Please Help! | The Lark Shift Consulting | Modern, Dynamic Website for a Social Enterprise

Calling for dynamic and modern designers! Please save me from the rut I am in with my current designer.

What is the business?
The Lark is a social enterprise. We are a private and public sector consultancy founded on the belief that we can leave the world a better place than the one we came into.

We are positioned as business consulting with a difference. We are creative problem solvers that aim to bring solutions that balance profits with purpose.

What we hope for:
Something modern, dynamic and inspiring. I see this one single page with the menu at the top or on the right, but feel free to propose more pages if required. I have done some work on visual style but I wouldn't consider myself an expert. I hope to see someone pick up from where I left off and take this to the next level. Alternatively, propose something totally new with gradients etc. I'm totally open and the sky is the limit :)

Background and references:
I have been trying to develop my website for a while now. I have been struggling with a wordpress web developer that has limited graphic design skills.

I have already done some thinking on this in working with my current designer (but please don't be constrained by the design aspects):

1. Check the PDF deck for content this also includes the sections of the website and subsections
2. Miro - I did a structural layout to illustrate to my current designer. This is not intended to be final design https://boardloft.example/app/board/kPqRT-Zz48L=/?share_link_id=91426385017
3. I even tried starting to design myself in frustration but please don't let this limit you https://www.sketchnest.example/design/QWJtuLpNZrx/HVBE4GmsYTaoRk7Lezi9Pn/edit?utm_content=QWJtuLpNZrx&utm_campaign=designshare&utm_medium=link2&utm_source=sharebutton

Target Market(s)

Forward-thinking consulting clients that care about making a difference in the world. These are both businesses and government agencies that are innovative and tired of the status quo of consulting

Industry/Entity Type

Social and Environmental Impact Consulting | Social Enterprise

Number of Pages Required

1 page

Font styles to use
Other font styles liked:
• I like Obibook with different line weights but open to other options

Requirements
Must have
• Please reflect on the entire content in the PDF for web and mobile. These are the proposed sections of the single page website. If you use imagery please be inspired by those in the PDF content deck and on the miro
Nice to have
• Unique graphics and icons
Should not have
• Corporate looking. Pictures of random business people. anything that looks boilerplate

```html
<!DOCTYPE html>
<html lang="en">
<head>
<meta charset="utf-8">
<title>The Lark Shift Consulting</title>
<link href="https://fonts.googleapis.com/css2?family=Poppins:wght@400;500;600;700;800&display=swap" rel="stylesheet">
<style>
:root{
  --ink:#151515;
  --orange:#f26522;
  --orange-deep:#e8531a;
  --amber:#f7a000;
  --teal:#1f8f8a;
  --mist:#f1f6f7;
  --white:#ffffff;
  --grey-text:#4a4a4a;
  --peach:#fbd3bd;
}
*{margin:0;padding:0;box-sizing:border-box}
html,body{width:1200px;height:4942px;overflow:hidden}
body{position:relative;background:var(--white);font-family:'Poppins',sans-serif;color:var(--ink)}
.abs{position:absolute}
.btn{position:absolute;display:flex;align-items:center;justify-content:center;border-radius:26px;font-size:13px;font-weight:700;letter-spacing:.5px;text-transform:uppercase}
.btn-orange{background:var(--orange);color:var(--white)}
.btn-white{background:var(--white);color:var(--ink)}
.eyebrow{position:absolute;font-size:20px;font-weight:600;text-transform:uppercase;letter-spacing:.5px}
.section-title{position:absolute;font-size:42px;font-weight:700;line-height:45px;text-transform:uppercase}
.center{left:0;width:1200px;text-align:center}
.art{position:absolute}

/* header */
.brand{left:90px;top:12px;width:170px;text-align:center}
.brand-name{font-size:30px;font-weight:800;letter-spacing:.5px;line-height:34px;border-bottom:3px solid var(--ink);padding-bottom:2px}
.brand-sub{font-size:10px;letter-spacing:1px;margin-top:5px;text-transform:uppercase}
.nav{left:317px;top:31px;display:flex;gap:29px;font-size:13px;font-weight:500}

/* hero */
.hero-kicker{left:88px;top:268px;font-size:38px;font-weight:700;letter-spacing:1px}
.hero-title{left:84px;top:300px;font-size:104px;font-weight:800;letter-spacing:2px;line-height:110px}
.hero-sub{left:88px;top:412px;font-size:23px;line-height:31px;color:#333}
.intro{left:643px;top:830px;width:480px;font-size:28px;font-weight:600;line-height:33px}

/* why section */
.why-eyebrow{left:90px;top:1316px;font-size:19px;font-weight:700;color:var(--white)}
.why-title{left:90px;top:1345px;font-size:42px;font-weight:700;line-height:45px;color:var(--white)}
.why-copy{left:90px;top:1446px;width:470px;font-size:14.5px;line-height:23px;color:var(--white)}
.why-copy p{margin-bottom:5px}

/* help */
.help-item{position:absolute;top:2212px;width:260px;text-align:center}
.help-icon{width:130px;height:115px;margin:0 auto;border-radius:50% 45% 50% 48%}
.help-label{margin-top:30px;font-size:22px;font-weight:700;line-height:27px}

/* impact */
.impact-list{left:271px;top:2834px;width:660px;list-style:none}
.impact-list li{height:36px;margin-bottom:7.5px;background:var(--white);box-shadow:0 2px 6px rgba(0,0,0,.09);display:flex;align-items:center;justify-content:space-between;padding:0 20px 0 26px;font-size:13px;font-weight:600}
.impact-list .plus{color:var(--teal);font-size:18px;font-weight:600}

/* clients */
.client{position:absolute;top:3556px;width:146px;height:146px;border-radius:50%;background:#f4f4f4;display:flex;align-items:center;justify-content:center;text-align:center;font-size:14px;font-weight:600;color:#3a3a3a;line-height:18px;padding:0 16px}

/* founder */
.founder-card{left:109px;top:4200px;width:248px;height:85px;background:var(--white);border-radius:14px;box-shadow:0 6px 18px rgba(0,0,0,.12);padding:20px 0 0 42px}
.founder-card .name{font-size:15px}
.founder-card .role{font-size:20px;font-weight:700}
.founder-copy{left:588px;top:4012px;width:490px;font-size:14.5px;line-height:23px;color:var(--grey-text)}
.founder-copy p{margin-bottom:8px}

/* footer */
.footer-brand{left:157px;top:4668px;width:256px;text-align:center;color:var(--white)}
.footer-brand .brand-name{font-size:44px;line-height:50px;border-bottom:4px solid;border-image:linear-gradient(90deg,var(--teal),#e62a1e) 1;padding-bottom:4px}
.footer-brand .brand-sub{font-size:15px;letter-spacing:1.5px;margin-top:10px}
.footer-col{top:4650px;color:var(--white)}
.footer-col h3{font-size:19px;font-weight:700;margin-bottom:6px}
.footer-col li{list-style:none;font-size:13px;line-height:24px}
.socials{display:flex;gap:12px;margin-top:8px}
.socials span{width:10px;height:10px;border-radius:50%;background:var(--white)}
.rule{left:88px;top:4890px;width:1024px;height:1px;background:#3a3a3a}
.copyright{left:0;width:1200px;top:4912px;text-align:center;font-size:12px;font-weight:500;color:var(--white)}
.to-top{left:1113px;top:4912px;width:40px;height:40px;border-radius:50%;background:linear-gradient(135deg,#c9b000,var(--orange))}
</style>
</head>
<body>

<!-- header -->
<div class="abs brand">
  <div class="brand-name">THE LARK</div>
  <div class="brand-sub">Shift Consulting</div>
</div>
<nav class="abs nav">
  <span>Why The Lark?</span><span>How we help?</span><span>What is our impact?</span><span>Who have we worked with?</span><span>Who is behind The Lark?</span>
</nav>

<!-- hero -->
<div class="abs hero-kicker">WHAT IS YOUR</div>
<div class="abs hero-title">MISSION</div>
<div class="abs hero-sub">Purpose Led Design, Strategy, Innovation<br>and Facilitation.</div>
<div class="btn btn-orange" style="left:88px;top:493px;width:167px;height:48px">Contact us</div>
<div class="art" role="img" aria-label="Line illustration of a yellow rocket launching out of a light bulb among stars and clouds" style="left:600px;top:140px;width:500px;height:560px;background:radial-gradient(ellipse at 55% 35%,#ffe08a 0,#fff3d0 30%,#ffffff 70%)"></div>

<div class="art" role="img" aria-label="Illustration of a woman holding a phone with speech bubbles and a planet" style="left:105px;top:690px;width:490px;height:423px;border-radius:48% 52% 40% 44%;background:linear-gradient(135deg,#fbc94a,#9fc18a 70%,#f7b49a)"></div>
<div class="abs intro">The Lark is a social and environmental impact consultancy focused on inspiring, defining, and bringing to life a more purposeful future.</div>

<!-- why section background -->
<svg class="abs" style="left:0;top:1080px" width="1200" height="900" viewBox="0 1080 1200 900">
  <defs>
    <linearGradient id="whyGrad" x1="0" y1="1" x2="1" y2="0">
      <stop offset="0" stop-color="#f7a000"/>
      <stop offset=".55" stop-color="#f07a10"/>
      <stop offset="1" stop-color="#e8531a"/>
    </linearGradient>
  </defs>
  <path d="M0 1165 C120 1140 230 1100 340 1110 C500 1125 640 1220 820 1230 C950 1238 1080 1200 1200 1190 L1200 1880 C1100 1905 1000 1880 900 1900 C780 1930 700 1975 620 1958 C520 1935 450 1840 350 1843 C230 1846 130 1935 0 1945 Z" fill="url(#whyGrad)"/>
  <path d="M860 1200 C940 1160 1120 1175 1200 1200 L1200 1840 C1100 1885 950 1900 820 1862 C660 1820 560 1700 575 1560 C590 1430 700 1385 780 1322 C822 1290 820 1240 860 1200 Z" fill="#0b0b0b"/>
</svg>
<div class="art" role="img" aria-label="Illustration of a person with glasses holding a glowing star in an open hand among space shapes" style="left:660px;top:1330px;width:520px;height:420px;border-radius:40%;background:radial-gradient(circle at 45% 45%,#f9b82a 0,#3a3a3a 35%,#0b0b0b 70%)"></div>

<div class="abs why-eyebrow">WHY THE LARK?</div>
<div class="abs why-title">WHY WAS THE<br>LARK FOUNDED?</div>
<div class="abs why-copy">
  <p>The Lark is a private and public sector consultancy founded on the belief that we can leave the world a better place than the one we came into.</p>
  <p>This is business consulting with a difference.</p>
  <p>We intend to bring your triple bottom line to life, maximizing profit, people, and planet. We believe in the power of purpose for achieving these outcomes.</p>
  <p>We meet you where you are, scale and pivot with you, all while being human and discovering the thrill of what it means to be us, the greatest wonder in the world.</p>
</div>
<div class="btn btn-white" style="left:88px;top:1701px;width:167px;height:48px">Read more</div>

<!-- how we help -->
<div class="eyebrow center" style="top:2074px;color:var(--teal)">How we help</div>
<div class="section-title center" style="top:2104px">We deliver purpose<br>driven...</div>
<div class="help-item" style="left:196px">
  <div class="help-icon" role="img" aria-label="Line icon of a head with a light bulb" style="background:#d6ece9"></div>
  <div class="help-label">Research and<br>Discovery</div>
</div>
<div class="help-item" style="left:469px">
  <div class="help-icon" role="img" aria-label="Line icon of chess pieces" style="background:#fbd8c9"></div>
  <div class="help-label">Strategy and<br>Innovation</div>
</div>
<div class="help-item" style="left:747px">
  <div class="help-icon" role="img" aria-label="Line icon of a handshake" style="background:#fde6b8"></div>
  <div class="help-label">Collaboration and<br>Facilitation</div>
</div>

<!-- impact background -->
<svg class="abs" style="left:0;top:2450px" width="1200" height="950" viewBox="0 2450 1200 950">
  <path d="M0 2560 C250 2540 400 2462 600 2466 C800 2470 950 2560 1200 2520 L1200 3330 C1000 3300 850 3390 650 3352 C450 3312 250 3392 0 3342 Z" fill="var(--mist)"/>
  <circle cx="702" cy="2540" r="37" fill="#d9d2ef"/>
  <circle cx="507" cy="2630" r="6" fill="#f2c230"/>
  <circle cx="146" cy="2780" r="6" fill="#2ed0cf"/>
  <circle cx="998" cy="2860" r="14" fill="#2ed0cf"/>
  <circle cx="1141" cy="3146" r="10" fill="#b08ce8"/>
  <circle cx="626" cy="3276" r="11" fill="#f2c230"/>
</svg>

<div class="eyebrow center" style="top:2696px;color:var(--teal)">What is our impact</div>
<div class="section-title center" style="top:2724px">What is some of<br>our impact?</div>
<ul class="abs impact-list">
  <li><span>Web 3 Business Design and Execution – Family Group, UAE</span><span class="plus">+</span></li>
  <li><span>Climate Change Systems Analysis – Harbour City Government, UAE</span><span class="plus">+</span></li>
  <li><span>National Healthcare Strategy – Regional Ministry of Health</span><span class="plus">+</span></li>
  <li><span>Human Centered -Volunteering Framework Capital Emirate Government, UAE</span><span class="plus">+</span></li>
  <li><span>Wellbeing Strategy – Community Futures Department (CFD), UAE</span><span class="plus">+</span></li>
  <li><span>Future Livability Model and Citizen of the Future – GCC Municipality, KSA</span><span class="plus">+</span></li>
  <li><span>Parent Wellbeing Program– Capital Emirate Government, UAE</span><span class="plus">+</span></li>
  <li><span>Innovation, Strategy &amp; Design Thinking Workshops – Across GCC</span><span class="plus">+</span></li>
</ul>

<!-- clients -->
<div class="eyebrow center" style="top:3460px;color:var(--amber)">How we help</div>
<div class="section-title center" style="top:3490px">Some of our clients</div>
<div class="client" style="left:144px">Arden Works</div>
<div class="client" style="left:299px">Little Steps Agency</div>
<div class="client" style="left:453px">Brightfund Lab</div>
<div class="client" style="left:607px">Norvale</div>
<div class="client" style="left:760px">Sable &amp; Co</div>
<div class="client" style="left:912px">Transit Hub</div>

<!-- founder -->
<svg class="abs" style="left:0;top:3780px" width="560" height="560" viewBox="0 0 560 560">
  <defs>
    <linearGradient id="arcGrad" x1="0" y1="0" x2="1" y2="1">
      <stop offset="0" stop-color="#fde3d2"/>
      <stop offset="1" stop-color="#f49a6a"/>
    </linearGradient>
  </defs>
  <path d="M60 40 C250 -10 470 40 530 200 C575 330 520 470 430 530 L400 500 C470 420 480 300 430 200 Z" fill="url(#arcGrad)"/>
</svg>
<div class="art" role="img" aria-label="Portrait photograph of the founder, smiling with long curly hair" style="left:0;top:3812px;width:498px;height:498px;border-radius:40% 55% 58% 20%;background:radial-gradient(circle at 45% 40%,#c98b6b 0,#6b3f2a 45%,#1e1410 80%)"></div>
<div class="abs founder-card">
  <div class="name">Maren Okafor</div>
  <div class="role">Founder Profile</div>
</div>
<div class="section-title" style="left:588px;top:3904px">Who is behind<br>the Lark?</div>
<div class="abs founder-copy">
  <p>Our founder, Maren, is an impact advisor, creator, and doer. Her sweet spot is at the nexus of purpose, strategy, and innovation.</p>
  <p>She has a strong passion for digitally-enabled social impact, bringing this to life in the private and public sectors. She thrives when working towards better outcomes in healthcare, entrepreneurship, social services, and sustainability.</p>
  <p>Lately, she has been working to develop meaningful Web 3 business models and managing teams to bring them to life.</p>
</div>
<div class="btn btn-orange" style="left:588px;top:4228px;width:167px;height:48px">Read more</div>

<!-- footer -->
<svg class="abs" style="left:0;top:4270px" width="1200" height="672" viewBox="0 4270 1200 672">
  <defs>
    <linearGradient id="edgeGrad" x1="0" y1="0" x2="1" y2="0">
      <stop offset="0" stop-color="#1f8f8a"/>
      <stop offset=".6" stop-color="#e0a21a"/>
      <stop offset="1" stop-color="#e62a1e"/>
    </linearGradient>
  </defs>
  <path d="M0 4400 C300 4440 700 4530 1000 4450 C1100 4420 1170 4350 1200 4300 L1200 4942 L0 4942 Z" fill="url(#edgeGrad)"/>
  <path d="M0 4410 C300 4455 700 4548 1000 4468 C1100 4440 1170 4375 1200 4330 L1200 4942 L0 4942 Z" fill="var(--ink)"/>
</svg>
<div class="abs footer-brand">
  <div class="brand-name">THE LARK</div>
  <div class="brand-sub">SHIFT CONSULTING</div>
</div>
<div class="abs footer-col" style="left:499px">
  <h3>USEFUL LINKS</h3>
  <ul>
    <li>Why The Lark?</li>
    <li>How we help?</li>
    <li>What is our impact?</li>
    <li>Who have we worked with?</li>
    <li>Who is behind The Lark?</li>
  </ul>
</div>
<div class="abs footer-col" style="left:783px">
  <h3>CONTACT US</h3>
  <ul>
    <li>maren@larkshiftconsulting.example</li>
    <li>+971 50 000 4812</li>
  </ul>
  <div class="socials"><span></span><span></span><span></span><span></span></div>
</div>
<div class="abs rule"></div>
<div class="abs copyright">©Copyright 2022 | All Rights Reserved</div>
<div class="abs to-top"></div>

</body>
</html>
```